Surviving Domestic Violence Flyer

I need a flyer that "POPS" to attract participants for my research project. I have added the important information on my draft flyer.

```html
<!DOCTYPE html>
<html lang="en">
<head>
<meta charset="utf-8">
<title>Request for Study Participants</title>
<link href="https://fonts.googleapis.com/css2?family=Oswald:wght@500&family=Roboto+Condensed:wght@700&family=Arimo:wght@400;700&display=swap" rel="stylesheet">
<style>
  :root {
    --page: #ffffff;
    --ink: #0b0b0b;
    --panel-top: #070707;
    --panel-mid: #151515;
    --teal: #17a9ad;
    --white: #ffffff;
    --soft-white: #f2f2f2;
    --photo-dark: #1c1e22;
    --photo-light: #8c9ca1;
    --photo-accent: #7a1a6a;
  }
  * { margin: 0; padding: 0; box-sizing: border-box; }
  html, body { width: 1200px; height: 900px; overflow: hidden; background: var(--page); }
  .flyer {
    position: absolute; left: 261px; top: 6px; width: 652px; height: 844px;
    background: linear-gradient(180deg, var(--panel-top) 0%, var(--panel-mid) 45%, #1d1d1d 80%);
    font-family: "Arimo", Arial, sans-serif; color: var(--white); overflow: hidden;
  }
  .flyer__title {
    position: absolute; top: 22px; left: 0; width: 100%; text-align: center;
    font-family: "Oswald", sans-serif; font-weight: 500; font-size: 50px;
    letter-spacing: 0.5px; color: var(--teal); line-height: 60px;
  }
  .flyer__subtitle {
    position: absolute; top: 85px; left: 0; width: 100%; text-align: center;
    font-family: "Roboto Condensed", sans-serif; font-weight: 700; font-size: 15px;
    letter-spacing: 0.4px; color: var(--white);
  }
  .photo {
    position: absolute; left: 0; top: 200px; width: 360px; height: 502px;
    background:
      radial-gradient(ellipse 45% 35% at 30% 45%, rgba(122,26,106,0.75), transparent 70%),
      radial-gradient(ellipse 80% 40% at 55% 95%, var(--photo-light), transparent 75%),
      linear-gradient(180deg, rgba(21,21,21,0) 0%, var(--photo-dark) 30%, #4a5559 100%);
  }
  .floor-glow {
    position: absolute; left: 0; top: 520px; width: 652px; height: 182px;
    background: linear-gradient(90deg, rgba(140,156,161,0.55) 0%, rgba(80,92,96,0.45) 55%, rgba(40,44,46,0.2) 100%);
  }
  .questions { position: absolute; left: 99px; top: 136px; width: 520px; list-style: none; }
  .questions li { font-size: 17px; line-height: 20px; margin-bottom: 12.5px; }
  .questions li:nth-child(odd) { color: var(--teal); }
  .questions li:nth-child(even) { color: var(--white); }
  .details { position: absolute; left: 320px; top: 356px; width: 310px; }
  .details__eligibility { font-size: 13px; line-height: 16.5px; color: var(--soft-white); }
  .details__contact { margin-top: 20px; font-size: 20px; line-height: 24px; }
  .details__phone { display: block; font-size: 26px; line-height: 32px; text-align: center; width: 290px; }
  .details__small { font-size: 11.5px; line-height: 14px; color: var(--soft-white); }
  .details__small a { color: var(--teal); text-decoration: none; }
  .details__email { margin-top: 6px; }
  .details__comp { margin-top: 14px; }
  .details__label { color: var(--teal); }
  .details__credits { margin-top: 14px; }
  .tearoffs {
    position: absolute; left: 0; top: 702px; width: 652px; height: 142px;
    background: var(--ink); border-top: 1px solid #777; display: flex;
  }
  .tearoff {
    flex: 1; position: relative; border-right: 1px solid #9a9a9a; margin-top: 6px;
  }
  .tearoff:last-child { border-right: none; }
  .tearoff__text {
    position: absolute; left: 50%; bottom: 6px; transform-origin: left bottom;
    transform: translate(-3px, 0) rotate(-90deg) translateY(100%);
    white-space: nowrap; line-height: 14px;
  }
  .tearoff__label { display: block; font-size: 9.5px; font-weight: 700; }
  .tearoff__phone { display: block; font-size: 13px; font-weight: 700; }
</style>
</head>
<body>
<main class="flyer">
  <div class="photo" role="img" aria-label="Photograph of a woman sitting on the floor hugging her knees while a hand rests on her shoulder"></div>
  <div class="floor-glow"></div>

  <h1 class="flyer__title">Request for Study Participants</h1>
  <p class="flyer__subtitle">EFFICIENCY OF RESOURCES AVAILABLE TO SUVIVORS OF INTIMATE PARTNER ABUSE</p>

  <ul class="questions">
    <li>Are you eighteen years of age or older?</li>
    <li>Have you been a victim of domestic violence?</li>
    <li>Have you sought assistance with abuse in last 12 months?</li>
    <li>Are you still in contact with person who abused you?</li>
    <li>Are you willing and open to discussing your expirience with abuse and your attempts to access services or resources?</li>
  </ul>

  <section class="details">
    <p class="details__eligibility">If you answered yes to all of these questions, you may be eligible to participate in a study to better understand the resources needed and services expected for survivors of domestic violence.</p>
    <p class="details__contact">Please contact Dana Whitfield at
      <span class="details__phone">1(555)014-2290</span></p>
    <p class="details__small details__email">via e-mail <a href="mailto:survivorvoices.study@example.org">survivorvoices.study@example.org</a><br>for additional information.</p>
    <p class="details__small details__comp">Participants will be comensated for their time.</p>
    <p class="details__small details__credits">
      <span class="details__label">Princinal Investigator</span><br>
      Dana Whitfield<br>
      Institutional Affiliation: Lakeshore State University<br>
      Dept. of Criminology, Law and Justice<br>
      <span class="details__label">Contact Address</span><br>
      Post Office Box 318204, Riverton, IL, 60699
    </p>
  </section>

  <div class="tearoffs">
    <div class="tearoff"><p class="tearoff__text"><span class="tearoff__label">Survivor Resources Study</span><span class="tearoff__phone">1(555)014-2290</span></p></div>
    <div class="tearoff"><p class="tearoff__text"><span class="tearoff__label">Survivor Resources Study</span><span class="tearoff__phone">1(555)014-2290</span></p></div>
    <div class="tearoff"><p class="tearoff__text"><span class="tearoff__label">Survivor Resources Study</span><span class="tearoff__phone">1(555)014-2290</span></p></div>
    <div class="tearoff"><p class="tearoff__text"><span class="tearoff__label">Survivor Resources Study</span><span class="tearoff__phone">1(555)014-2290</span></p></div>
    <div class="tearoff"><p class="tearoff__text"><span class="tearoff__label">Survivor Resources Study</span><span class="tearoff__phone">1(555)014-2290</span></p></div>
    <div class="tearoff"><p class="tearoff__text"><span class="tearoff__label">Survivor Resources Study</span><span class="tearoff__phone">1(555)014-2290</span></p></div>
    <div class="tearoff"><p class="tearoff__text"><span class="tearoff__label">Survivor Resources Study</span><span class="tearoff__phone">1(555)014-2290</span></p></div>
    <div class="tearoff"><p class="tearoff__text"><span class="tearoff__label">Survivor Resources Study</span><span class="tearoff__phone">1(555)014-2290</span></p></div>
    <div class="tearoff"><p class="tearoff__text"><span class="tearoff__label">Survivor Resources Study</span><span class="tearoff__phone">1(555)014-2290</span></p></div>
    <div class="tearoff"><p class="tearoff__text"><span class="tearoff__label">Survivor Resources Study</span><span class="tearoff__phone">1(555)014-2290</span></p></div>
    <div class="tearoff"><p class="tearoff__text"><span class="tearoff__label">Survivor Resources Study</span><span class="tearoff__phone">1(555)014-2290</span></p></div>
    <div class="tearoff"><p class="tearoff__text"><span class="tearoff__label">Survivor Resources Study</span><span class="tearoff__phone">1(555)014-2290</span></p></div>
    <div class="tearoff"><p class="tearoff__text"><span class="tearoff__label">Survivor Resources Study</span><span class="tearoff__phone">1(555)014-2290</span></p></div>
  </div>
</main>
</body>
</html>
```